Create a Powerpoint presentation pack with our new logo

We have just selected a new logo using ArtHive and we were wanting to create a new Powerpoint presentation pack using this logo.
We'd like the powerpoint pack to have a title page + a header and footer page.
We would like the logo to appear on the title page and the header / footer page.
We are flexible with colours and want something that reflects an IT / travel flair.

I have attached the logo that we just selected from the arthive page.

Palomar Vista Systems is the IT division of Palomar Vista Journeys Group which is the largest travel retailer in Australia. We have offices in the US, Canada, UK, Singapore, Hong Kong, UAE, India, South Africa, Mexico and New Zealand.

```html
<!DOCTYPE html>
<html lang="en">
<head>
<meta charset="utf-8">
<title>Palomar Vista Systems – Presentation Pack</title>
<link href="https://fonts.googleapis.com/css2?family=Roboto:wght@300;400;500;700&display=swap" rel="stylesheet">
<style>
:root{
  --stage:#5b5b5b;
  --red:#e31e24;
  --red-deep:#c9151b;
  --ink:#333333;
  --dark:#454545;
  --grey:#8a8a8a;
  --light:#e3e3e3;
  --white:#ffffff;
  --black:#1a1a1a;
}
*{margin:0;padding:0;box-sizing:border-box}
html,body{width:1200px;height:689px;overflow:hidden;background:var(--stage);font-family:"Roboto",Arial,sans-serif;color:var(--ink)}
h1,h2,p{font-weight:inherit}
.canvas{position:relative;width:1200px;height:689px}
.slide{position:absolute;width:380px;height:210px;overflow:hidden;background:var(--white);font-weight:400}
.col-1{left:10px}.col-2{left:406px}.col-3{left:808px}
.row-1{top:10px}.row-2{top:236px}.row-3{top:462px}

/* brand */
.brand{position:absolute;display:flex;align-items:center;gap:4px;font-weight:700;white-space:nowrap}
.brand-dot{width:13px;height:13px;border-radius:50%;border:1.5px solid currentColor}
.brand-red{color:var(--red);font-size:7.5px;top:12px;right:10px}
.brand-white{color:var(--white);font-size:7.5px;top:12px;right:10px}
.brand-title{color:var(--red);font-size:14px;left:0;right:0;justify-content:center;top:170px;gap:7px}
.brand-title .brand-dot{width:24px;height:24px;border-width:2.5px}

/* shared header/footer */
.kicker{position:absolute;left:12px;top:8px;font-size:4.5px;letter-spacing:1px;color:#b5b5b5;text-transform:uppercase}
.page-title{position:absolute;left:12px;top:17px;font-size:10px;letter-spacing:.6px;color:var(--ink);font-weight:400}
.title-rule{position:absolute;left:12px;top:32px;width:22px;height:2px;background:var(--red)}
.footer-rule{position:absolute;left:0;right:0;top:190px;height:1px;background:#ececec}
.footer-url,.footer-num{position:absolute;top:197px;font-size:6.5px;color:var(--grey)}
.footer-url{left:8px}.footer-num{right:10px}
.fine{font-size:3.8px;line-height:5.2px;color:#777}

/* title slide */
.title-band{position:absolute;left:0;top:0;width:100%;height:124px;background:var(--red)}
.title-main{position:absolute;top:52px;width:100%;text-align:center;color:var(--white);font-weight:700;font-size:16px}
.title-sub{position:absolute;top:77px;width:100%;text-align:center;color:var(--white);font-weight:300;font-size:10px}
.title-base{position:absolute;left:0;bottom:0;width:100%;height:6px;background:var(--black)}

/* quote slides */
.fill-red{background:var(--red)}
.quote{position:absolute;left:40px;right:40px;text-align:center;color:var(--white);font-size:8px;line-height:11.5px;font-weight:400}
.quote-by{position:absolute;left:0;right:0;text-align:center;color:var(--white);font-size:8px;font-weight:400}
.photo-people{position:absolute;inset:0;background:linear-gradient(120deg,#3d3d3d,#7a7a7a 45%,#4a4a4a)}
.photo-text{position:absolute;left:48px;right:36px;top:90px;text-align:center;color:var(--white);font-size:8px;line-height:11.5px;font-weight:400}
.page-num-light{position:absolute;right:10px;bottom:6px;font-size:6px;color:var(--white)}

/* agenda grid */
.agenda-item{position:absolute;width:86px}
.agenda-head{display:flex;align-items:center;gap:6px;font-size:6.3px;font-weight:500}
.agenda-head.red{color:var(--red)}
.agenda-head.dark{color:var(--ink)}
.icon{width:22px;height:22px;border-radius:50%;display:flex;align-items:center;justify-content:center;flex:none}
.icon.red{background:var(--red)}
.icon.dark{background:var(--dark)}
.icon svg{width:10px;height:10px}
.agenda-item .fine{margin-top:8px}

/* icon slide */
.feature{position:absolute;top:48px;width:70px;text-align:center}
.feature .icon{width:38px;height:38px;margin:0 auto}
.feature .icon svg{width:16px;height:16px}
.feature-label{margin-top:8px;font-size:6px}
.feature-label.red{color:var(--red)}
.feature .fine{margin-top:7px}

/* divider */
.photo-city{position:absolute;inset:0;background:linear-gradient(180deg,#d8262c 0%,#c81d23 55%,#a8151a 100%)}
.divider-title{position:absolute;top:86px;width:100%;text-align:center;color:var(--white);font-size:17px;font-weight:400;letter-spacing:.4px}

/* details */
.photo-building{position:absolute;left:0;top:0;width:178px;height:210px;background:linear-gradient(135deg,#2b2b2b,#9a9a9a 50%,#444)}
.details-panel{position:absolute;left:178px;top:0;width:202px;height:210px;background:var(--red)}
.details-title{position:absolute;left:19px;top:40px;color:var(--white);font-size:13.5px;font-weight:400}
.details-copy{position:absolute;left:19px;width:172px;color:var(--white);font-size:8px;line-height:11.2px;font-weight:400}

/* steps */
.step{position:absolute;left:54px;width:300px;height:26px}
.step svg{position:absolute;left:0;top:0}
.step-copy{position:absolute;left:57px;top:-2px;width:235px}
.step-title{font-size:5.6px;font-weight:500;color:var(--ink);margin-bottom:2px}

/* data */
.map-area{position:absolute;left:36px;top:43px;width:132px;height:111px;border-radius:40% 30% 45% 35%;background:linear-gradient(160deg,#d5d5d5,#e4e4e4)}
.map-pill{position:absolute;left:64px;top:92px;width:72px;height:28px;border-radius:14px;background:var(--red);color:var(--white);font-size:12.5px;font-weight:500;display:flex;align-items:center;justify-content:center}
.stat{position:absolute;top:162px;display:flex;align-items:center;gap:4px}
.stat .icon{width:17px;height:17px}
.stat-num{font-size:8px;font-weight:500;color:var(--red);line-height:9px}
.stat-label{font-size:3.5px;color:var(--grey)}
.chart-title{position:absolute;left:194px;top:44px;font-size:5px;font-weight:500}
.chart-note{position:absolute;left:194px;top:53px;width:175px}
.chart{position:absolute;left:194px;top:82px}
.chart-foot{position:absolute;left:196px;top:156px;width:170px;padding-left:5px;border-left:1px solid #ccc}
</style>
</head>
<body>
<div class="canvas">

  <!-- Title -->
  <section class="slide col-1 row-1">
    <div class="title-band"></div>
    <h1 class="title-main">PROJECT TITLE HERE</h1>
    <p class="title-sub">Subtext here Subtext here</p>
    <div class="brand brand-title"><span class="brand-dot"></span>Palomar Vista Systems</div>
    <div class="title-base"></div>
  </section>

  <!-- Quote -->
  <section class="slide col-2 row-1 fill-red">
    <div class="brand brand-white"><span class="brand-dot"></span>Palomar Vista Systems</div>
    <p class="quote" style="top:94px">"Our investment approach focuses on partnering with brands which are in the rollout phase that require capital and local expertise to successfully enter and grow in internation markets"</p>
    <p class="quote-by" style="top:138px">Project Owner Name &nbsp;||&nbsp; Founder &amp; CEO</p>
  </section>

  <!-- Photo statement -->
  <section class="slide col-3 row-1">
    <div class="photo-people" role="img" aria-label="Greyscale photo of a group of smiling friends taking a selfie"></div>
    <div class="brand brand-white"><span class="brand-dot"></span>Palomar Vista Systems</div>
    <p class="photo-text">Liquorice candy drops &nbsp;cake applicake apple pie cupcake brownie bear claw Liquorice candy drops &nbsp;cake applicake apple pie cupcake brownie bear claw Liquorice candy drops &nbsp;cake applicake apple pie cupcake brownie bear claw Liquorice candy drops &nbsp;cake applicake</p>
    <span class="page-num-light">01</span>
  </section>

  <!-- Agenda grid -->
  <section class="slide col-1 row-2">
    <span class="kicker">Section One</span>
    <h2 class="page-title">Our Agenda</h2>
    <span class="title-rule"></span>
    <div class="brand brand-red"><span class="brand-dot"></span>Palomar Vista Systems</div>

    <div class="agenda-item" style="left:27px;top:47px">
      <div class="agenda-head red"><span class="icon red"><svg viewBox="0 0 10 10"><rect x="1.5" y="1.5" width="7" height="7" rx="1" fill="#fff"/><path d="M3 5l1.5 1.5L7 3.5" stroke="#e31e24" stroke-width="1.2" fill="none"/></svg></span>Creative Strategy</div>
      <p class="fine">Short notes on this topic go here with a brief plan summary for the team. Add key points, owners and dates so all can follow.</p>
    </div>
    <div class="agenda-item" style="left:147px;top:47px">
      <div class="agenda-head red"><span class="icon red"><svg viewBox="0 0 10 10"><rect x="1" y="1.5" width="8" height="5.5" fill="none" stroke="#fff" stroke-width="1.2"/><path d="M3.5 9h3M5 7v2" stroke="#fff" stroke-width="1.2"/></svg></span>Employee Desktop</div>
      <p class="fine">Short notes on this topic go here with a brief plan summary for the team. Add key points, owners and dates so all can follow.</p>
    </div>
    <div class="agenda-item" style="left:265px;top:47px">
      <div class="agenda-head red"><span class="icon red"><svg viewBox="0 0 10 10"><circle cx="3" cy="4" r="1.8" fill="#fff"/><circle cx="7" cy="4" r="1.8" fill="#fff"/><path d="M4.6 4.2L3 8M8.6 4.2L7 8" stroke="#fff" stroke-width="1"/></svg></span>Business Plan</div>
      <p class="fine">Short notes on this topic go here with a brief plan summary for the team. Add key points, owners and dates so all can follow.</p>
    </div>
    <div class="agenda-item" style="left:27px;top:122px">
      <div class="agenda-head dark"><span class="icon dark"><svg viewBox="0 0 10 10"><path d="M5 1l3.5 1.3v2.8C8.5 7.3 7 8.5 5 9.2 3 8.5 1.5 7.3 1.5 5.1V2.3z" fill="#fff"/></svg></span>System Protection</div>
      <p class="fine">Short notes on this topic go here with a brief plan summary for the team. Add key points, owners and dates so all can follow.</p>
    </div>
    <div class="agenda-item" style="left:147px;top:122px">
      <div class="agenda-head dark"><span class="icon dark"><svg viewBox="0 0 10 10"><rect x="1" y="3" width="8" height="4.5" rx="2.2" fill="#fff"/><circle cx="3.3" cy="5.2" r=".8" fill="#454545"/><circle cx="6.7" cy="5.2" r=".8" fill="#454545"/></svg></span>Fun Games</div>
      <p class="fine">Short notes on this topic go here with a brief plan summary for the team. Add key points, owners and dates so all can follow.</p>
    </div>
    <div class="agenda-item" style="left:265px;top:122px">
      <div class="agenda-head dark"><span class="icon dark"><svg viewBox="0 0 10 10"><path d="M5 1v5M3 4l2 2 2-2M1.5 8.5h7" stroke="#fff" stroke-width="1.2" fill="none"/></svg></span>Data Analysis</div>
      <p class="fine">Short notes on this topic go here with a brief plan summary for the team. Add key points, owners and dates so all can follow.</p>
    </div>

    <span class="footer-rule"></span>
    <span class="footer-url">www.palomarvista.com</span>
    <span class="footer-num">01</span>
  </section>

  <!-- Visual icons -->
  <section class="slide col-2 row-2">
    <span class="kicker">Section One</span>
    <h2 class="page-title" style="font-size:8px;top:19px">Creative Visual Icons</h2>
    <span class="title-rule"></span>
    <div class="brand brand-red"><span class="brand-dot"></span>Palomar Vista Systems</div>

    <div class="feature" style="left:19px">
      <span class="icon red"><svg viewBox="0 0 10 10"><rect x="1" y="1.5" width="8" height="5.5" fill="none" stroke="#fff" stroke-width="1.1"/><path d="M3.5 9h3M5 7v2" stroke="#fff" stroke-width="1.1"/></svg></span>
      <p class="feature-label red">Desktop Application</p>
      <p class="fine">Short notes on this idea go here. Keep each point clear and brief so the team can scan the plan and act on it fast without delay. Add owners, dates and the result you expect, then share it with the wider group for review.</p>
    </div>
    <div class="feature" style="left:101px">
      <span class="icon red"><svg viewBox="0 0 10 10"><ellipse cx="5" cy="5.8" rx="2.3" ry="3" fill="#fff"/><path d="M1.5 4h7M1.5 7h7M3.5 1.5l1 1.5M6.5 1.5l-1 1.5" stroke="#fff" stroke-width=".9"/></svg></span>
      <p class="feature-label red">Business Strategy</p>
      <p class="fine">Short notes on this idea go here. Keep each point clear and brief so the team can scan the plan and act on it fast without delay. Add owners, dates and the result you expect, then share it with the wider group for review.</p>
    </div>
    <div class="feature" style="left:183px">
      <span class="icon dark"><svg viewBox="0 0 10 10"><path d="M5 1l3.5 1.3v2.8C8.5 7.3 7 8.5 5 9.2 3 8.5 1.5 7.3 1.5 5.1V2.3z" fill="#fff"/></svg></span>
      <p class="feature-label">Sales Booster</p>
      <p class="fine">Short notes on this idea go here. Keep each point clear and brief so the team can scan the plan and act on it fast without delay. Add owners, dates and the result you expect, then share it with the wider group for review.</p>
    </div>
    <div class="feature" style="left:264px">
      <span class="icon dark"><svg viewBox="0 0 10 10"><path d="M8.5 1.5C6 1.7 4 3.5 3.2 6l.8.8C6.5 6 8.3 4 8.5 1.5zM3 5.5L1.5 6l1.2 1.3M4.5 7L4 8.5 2.7 7.3" fill="#fff"/></svg></span>
      <p class="feature-label">Concept &amp; Ideas</p>
      <p class="fine">Short notes on this idea go here. Keep each point clear and brief so the team can scan the plan and act on it fast without delay. Add owners, dates and the result you expect, then share it with the wider group for review.</p>
    </div>

    <span class="footer-rule"></span>
    <span class="footer-url">www.palomarvista.com</span>
  </section>

  <!-- Section divider -->
  <section class="slide col-3 row-2">
    <div class="photo-city" role="img" aria-label="City skyline photo washed in red"></div>
    <div class="brand brand-white" style="font-size:9px"><span class="brand-dot" style="width:16px;height:16px"></span>Palomar Vista Systems</div>
    <h2 class="divider-title">IMAGE &nbsp;SECTION DIVIDER</h2>
    <p class="quote" style="top:112px;left:30px;right:30px">"Our investment approach focuses on partnering with brands which are in the rollout phase that require capital and local expertise to successfully enter and grow in internation markets"</p>
  </section>

  <!-- Section details -->
  <section class="slide col-1 row-3">
    <div class="photo-building" role="img" aria-label="Greyscale photo looking up at a tall office building"></div>
    <div class="details-panel">
      <h2 class="details-title">IMAGE &nbsp;SECTION DETAILS</h2>
      <p class="details-copy" style="top:63px">Our investment approach focuses on part-nering with brands which are in the rollout phase that require capital and local exper-tise to successfully enter and grow in inter-nation markets.</p>
      <p class="details-copy" style="top:131px">Our investment approach focuses on part-nering with brands which are in the rollout phase that require capital and local exper-tise to successfully enter and grow in inter-nation markets"</p>
    </div>
  </section>

  <!-- Steps agenda -->
  <section class="slide col-2 row-3">
    <span class="kicker">Section One</span>
    <h2 class="page-title">Our Agenda</h2>
    <span class="title-rule"></span>
    <div class="brand brand-red"><span class="brand-dot"></span>Palomar Vista Systems</div>

    <div class="step" style="top:45px">
      <svg width="50" height="26" viewBox="0 0 50 26"><polygon points="0,0 40,0 50,13 40,26 0,26 8,13" fill="#e31e24"/><text x="25" y="17" text-anchor="middle" font-family="Roboto,Arial,sans-serif" font-size="11" font-weight="500" fill="#fff">1</text></svg>
      <div class="step-copy"><p class="step-title">Creative Strategy</p><p class="fine">A short summary of this step goes here. It sets out the goal, the owner, the timing and the result we expect the team to deliver. Add the key tasks, the budget and any risks to watch, then note how progress will be checked and shared with the wider group each week.</p></div>
    </div>
    <div class="step" style="top:82px">
      <svg width="50" height="26" viewBox="0 0 50 26"><polygon points="0,0 40,0 50,13 40,26 0,26 8,13" fill="#a8a8a8"/><text x="25" y="17" text-anchor="middle" font-family="Roboto,Arial,sans-serif" font-size="11" font-weight="500" fill="#fff">2</text></svg>
      <div class="step-copy"><p class="step-title">Boost Sales</p><p class="fine">A short summary of this step goes here. It sets out the goal, the owner, the timing and the result we expect the team to deliver. Add the key tasks, the budget and any risks to watch, then note how progress will be checked and shared with the wider group each week.</p></div>
    </div>
    <div class="step" style="top:119px">
      <svg width="50" height="26" viewBox="0 0 50 26"><polygon points="0,0 40,0 50,13 40,26 0,26 8,13" fill="#7a7a7a"/><text x="25" y="17" text-anchor="middle" font-family="Roboto,Arial,sans-serif" font-size="11" font-weight="500" fill="#fff">3</text></svg>
      <div class="step-copy"><p class="step-title">Global Brand Strategy</p><p class="fine">A short summary of this step goes here. It sets out the goal, the owner, the timing and the result we expect the team to deliver. Add the key tasks, the budget and any risks to watch, then note how progress will be checked and shared with the wider group each week.</p></div>
    </div>
    <div class="step" style="top:156px">
      <svg width="50" height="26" viewBox="0 0 50 26"><polygon points="0,0 40,0 50,13 40,26 0,26 8,13" fill="#454545"/><text x="25" y="17" text-anchor="middle" font-family="Roboto,Arial,sans-serif" font-size="11" font-weight="500" fill="#fff">4</text></svg>
      <div class="step-copy"><p class="step-title">Business Strategy</p><p class="fine">A short summary of this step goes here. It sets out the goal, the owner, the timing and the result we expect the team to deliver. Add the key tasks, the budget and any risks to watch, then note how progress will be checked and shared with the wider group each week.</p></div>
    </div>

    <span class="footer-url" style="top:198px">www.palomarvista.com</span>
    <span class="footer-num" style="top:198px">01</span>
  </section>

  <!-- Visual design / data -->
  <section class="slide col-3 row-3">
    <span class="kicker">Section One</span>
    <h2 class="page-title" style="font-size:8px;top:19px">Creative Visual Design</h2>
    <span class="title-rule"></span>
    <div class="brand brand-red"><span class="brand-dot"></span>Palomar Vista Systems</div>

    <div class="map-area" role="img" aria-label="Grey map of North America"></div>
    <div class="map-pill">359 M</div>
    <div class="stat" style="left:46px">
      <span class="icon red"><svg viewBox="0 0 10 10"><circle cx="5" cy="2" r="1.3" fill="#fff"/><rect x="3.6" y="3.8" width="2.8" height="5" rx=".6" fill="#fff"/></svg></span>
      <div><p class="stat-num">1.908 K</p><p class="stat-label">Male User</p></div>
    </div>
    <div class="stat" style="left:106px">
      <span class="icon red"><svg viewBox="0 0 10 10"><circle cx="5" cy="2" r="1.3" fill="#fff"/><polygon points="5,3.6 7.5,8.8 2.5,8.8" fill="#fff"/></svg></span>
      <div><p class="stat-num">2.074 K</p><p class="stat-label">Female User</p></div>
    </div>

    <p class="chart-title">Data Analysis</p>
    <p class="chart-note fine">Short notes on the data go here with key trends and a brief read on growth. Add the main driver behind each year and what the team should do next with it.</p>
    <svg class="chart" width="180" height="70" viewBox="0 0 180 70" font-family="Roboto,Arial,sans-serif" font-size="4" fill="#777">
      <line x1="10" y1="4" x2="10" y2="56" stroke="#ccc" stroke-width=".6"/>
      <line x1="10" y1="56" x2="136" y2="56" stroke="#ccc" stroke-width=".6"/>
      <text x="2" y="6">5</text><text x="2" y="16.5">4</text><text x="2" y="27">3</text><text x="2" y="37.4">2</text><text x="2" y="47.8">1</text><text x="2" y="58">0</text>
      <rect x="18" y="19.6" width="12" height="36.4" fill="#e31e24"/>
      <rect x="44" y="30" width="12" height="26" fill="#e31e24"/>
      <rect x="70" y="19.6" width="12" height="36.4" fill="#e31e24"/>
      <rect x="94" y="9.2" width="12" height="46.8" fill="#454545"/>
      <rect x="120" y="16.5" width="12" height="39.5" fill="#454545"/>
      <text x="24" y="66" text-anchor="middle">2010</text><text x="50" y="66" text-anchor="middle">2011</text><text x="76" y="66" text-anchor="middle">2012</text><text x="100" y="66" text-anchor="middle">2013</text><text x="126" y="66" text-anchor="middle">2014</text>
    </svg>
    <p class="chart-foot fine">Short notes on the data go here with key trends and a brief read on growth. Add the main driver behind each year and the next step.</p>

    <span class="footer-url" style="top:198px">www.palomarvista.com</span>
  </section>

</div>
</body>
</html>
```